Stationary for Oil & Gas Company
Valmora Engineering
Project: Stationary for Oil & Gas Company
Stationary for Oil & Gas Company - Energy
Creative Brief
Professional
Peter Hawley
Managing Director
18 Upper Fennick Road London E9 3LQ United Kingdom
peter.hawley@valmora-example.com
www.valmora-example.com
We need a design for business cards, letters, envelopes, folders and other presentation material.
Company name and/or logo

```html
<!DOCTYPE html>
<html lang="en">
<head>
<meta charset="utf-8">
<title>Valmora Engineering – Business Card</title>
<link href="https://fonts.googleapis.com/css2?family=Montserrat:wght@700&family=Open+Sans:wght@300;400&display=swap" rel="stylesheet">
<style>
  :root {
    --page-bg: #e9e7e4;
    --card-white: #ffffff;
    --brand-teal: #6c9c9a;
    --brand-orange: #f07a22;
    --ink-dark: #2a2e33;
    --ink-light: #f4f8f8;
  }
  * { margin: 0; padding: 0; box-sizing: border-box; }
  html, body {
    width: 1200px; height: 901px; overflow: hidden;
    background: var(--page-bg);
  }
  .canvas {
    position: relative; width: 1200px; height: 901px;
    display: flex; align-items: center; justify-content: center;
  }
  .business-card {
    position: relative; width: 900px; height: 515px;
    border-radius: 34px; overflow: hidden;
    background: var(--card-white);
    box-shadow: 0 18px 40px rgba(0,0,0,0.18);
  }
  .card-shapes { position: absolute; inset: 0; }
  .brand-block {
    position: absolute; left: 64px; top: 196px;
    display: flex; align-items: center; gap: 16px;
  }
  .brand-square {
    width: 34px; height: 34px; background: var(--brand-orange); flex: none;
  }
  .brand-name {
    display: flex; flex-direction: column;
    font-family: "Montserrat", sans-serif; font-weight: 700;
    text-transform: uppercase; color: var(--ink-dark); line-height: 1;
  }
  .brand-name-main { font-size: 50px; letter-spacing: 1px; }
  .brand-name-sub { font-size: 17px; letter-spacing: 8.4px; margin-top: 10px; }
  .contact-panel {
    position: absolute; left: 560px; top: 70px; width: 310px;
    color: var(--ink-light);
    font-family: "Open Sans", sans-serif; font-weight: 300;
  }
  .person-name {
    font-size: 24px; font-weight: 400; letter-spacing: 2px;
    text-transform: uppercase;
  }
  .person-title {
    font-size: 15px; letter-spacing: 2px; text-transform: uppercase;
    margin-top: 4px;
  }
  .postal-address {
    font-size: 17px; font-style: normal; line-height: 1.4;
    margin-top: 46px;
  }
  .contact-list { list-style: none; margin-top: 30px; }
  .contact-item {
    display: flex; align-items: center; gap: 14px;
    font-size: 15px; line-height: 1; margin-bottom: 14px;
  }
  .contact-icon { width: 18px; height: 18px; flex: none; }
</style>
</head>
<body>
<main class="canvas">
  <section class="business-card">
    <svg class="card-shapes" viewBox="0 0 900 515" aria-hidden="true">
      <path d="M470 -5 C540 150 545 360 505 520 L905 520 L905 -5 Z" fill="var(--brand-teal)"/>
      <path d="M438 -5 C505 150 512 360 472 520 L482 520 C524 360 518 150 452 -5 Z" fill="var(--brand-orange)"/>
      <path d="M458 -5 C526 150 532 360 492 520 L500 520 C540 360 536 150 466 -5 Z" fill="var(--card-white)"/>
    </svg>

    <div class="brand-block">
      <span class="brand-square"></span>
      <span class="brand-name">
        <span class="brand-name-main">Valmora</span>
        <span class="brand-name-sub">Engineering</span>
      </span>
    </div>

    <div class="contact-panel">
      <h1 class="person-name">Peter Hawley</h1>
      <p class="person-title">Financial Adviser</p>
      <address class="postal-address">18 Upper Fennick Road<br>London E9 3LQ</address>
      <ul class="contact-list">
        <li class="contact-item">
          <svg class="contact-icon" viewBox="0 0 24 24"><path fill="currentColor" d="M6.6 10.8a15 15 0 0 0 6.6 6.6l2.2-2.2c.3-.3.7-.4 1-.2 1.1.4 2.3.6 3.6.6.6 0 1 .4 1 1V20c0 .6-.4 1-1 1A17 17 0 0 1 3 4c0-.6.4-1 1-1h3.5c.6 0 1 .4 1 1 0 1.3.2 2.5.6 3.6.1.3 0 .7-.2 1z"/></svg>
          020 7946 0182
        </li>
        <li class="contact-item">
          <svg class="contact-icon" viewBox="0 0 24 24"><rect x="6" y="2" width="12" height="20" rx="2" fill="none" stroke="currentColor" stroke-width="2"/><circle cx="12" cy="18" r="1.3" fill="currentColor"/></svg>
          020 7946 0347
        </li>
        <li class="contact-item">
          <svg class="contact-icon" viewBox="0 0 24 24"><rect x="5" y="3" width="14" height="18" rx="1.5" fill="none" stroke="currentColor" stroke-width="2"/><path d="M8 8h8M8 12h8M8 16h5" stroke="currentColor" stroke-width="2"/></svg>
          020 7946 0591
        </li>
        <li class="contact-item">
          <svg class="contact-icon" viewBox="0 0 24 24"><rect x="2" y="5" width="20" height="14" rx="2" fill="none" stroke="currentColor" stroke-width="2"/><path d="M3 6l9 7 9-7" fill="none" stroke="currentColor" stroke-width="2"/></svg>
          peter.hawley@valmora-example.com
        </li>
      </ul>
    </div>
  </section>
</main>
</body>
</html>
```